i need a template design for online store

hi great designers, i need a template for any online store. But preferably well owned shopping carts. I would be an added advantage if the store is setup for me. I need a mature and attractive colours. My online store deals in electronics.

Shopping

1 page

```html
<!DOCTYPE html>
<html lang="en">
<head>
<meta charset="utf-8">
<title>Voltrix Store – Electronics</title>
<link href="https://fonts.googleapis.com/css2?family=Open+Sans:ital,wght@0,300;0,400;0,600;0,700;1,400;1,600&display=swap" rel="stylesheet">
<style>
:root{
  --teal:#1bb39a;
  --teal-dark:#17a28b;
  --ink:#1f1f1f;
  --text:#333333;
  --muted:#8a8a8a;
  --page:#ebebeb;
  --band:#d9d9d9;
  --head:#e6e6e6;
  --white:#ffffff;
  --black:#111111;
  --bar:#1d1d1d;
  --line:#d2d2d2;
  --btn-gray:#767676;
}
*{box-sizing:border-box;margin:0;padding:0}
html,body{width:1200px;height:3232px;overflow:hidden}
body{position:relative;background:var(--page);font-family:'Open Sans',sans-serif;color:var(--text)}
svg{display:block}

/* top bar */
.topbar{position:absolute;left:0;top:0;width:1200px;height:47px;background:var(--bar);color:#d8d8d8;font-size:14px}
.topbar .phone{position:absolute;left:50px;top:0;height:47px;display:flex;align-items:center;gap:10px;color:#eee}
.topbar .links{position:absolute;right:178px;top:0;height:47px;display:flex;align-items:center;font-size:11px;text-transform:uppercase;letter-spacing:.2px}
.topbar .links span{padding:0 8px;border-left:1px solid #555;line-height:12px}
.topbar .links span:first-child{border:none;color:var(--teal)}
.topbar .links .cart-total{color:var(--teal);font-style:normal}
.checkout{position:absolute;left:1040px;top:5px;width:108px;height:37px;background:var(--teal);color:#fff;font-size:12px;font-weight:600;display:flex;align-items:center;justify-content:center;gap:6px}

/* header */
.masthead{position:absolute;left:0;top:47px;width:1200px;height:115px;background:var(--head)}
.brand{position:absolute;left:54px;top:32px;font-size:36px;font-weight:700;color:var(--teal);letter-spacing:1px}
.search{position:absolute;left:685px;top:44px;display:flex}
.search .field{width:276px;height:34px;background:#fff;border:1px solid #d0d0d0;font-size:11px;color:#999;padding:9px 10px}
.search .go{width:64px;height:34px;background:#333;color:#fff;font-size:11px;font-weight:600;display:flex;align-items:center;justify-content:center}
.currency{position:absolute;left:1051px;top:44px;width:95px;height:34px;border:1px solid #d0d0d0;background:#ececec;font-size:10px;color:#999;display:flex;align-items:center;justify-content:center;gap:6px}

/* nav */
.mainnav{position:absolute;left:0;top:162px;width:1200px;height:49px;background:var(--black)}
.cat-toggle{position:absolute;left:50px;top:0;width:286px;height:49px;background:var(--teal);color:#fff;display:flex;align-items:center;gap:22px;padding-left:30px;font-size:20px;font-weight:600}
.navlinks{position:absolute;left:355px;top:0;display:flex;height:49px}
.navlinks a{height:49px;display:flex;align-items:center;justify-content:center;color:#fff;font-size:11px;font-weight:600;text-decoration:none;border-left:1px solid #333}
.navlinks a:first-child{border:none}

/* hero band */
.heroband{position:absolute;left:0;top:211px;width:1200px;height:511px;background:var(--band)}
.catlist{position:absolute;left:50px;top:211px;width:286px;height:511px;background:#fff;list-style:none}
.catlist li{height:56.7px;border-bottom:1px solid #e4e4e4;display:flex;align-items:center;padding-left:28px;font-size:12px;color:#333;text-transform:uppercase}
.catlist li.active{color:var(--teal)}
.hero{position:absolute;left:355px;top:233px;width:797px;height:471px;background:#fff}
.hero .copy{position:absolute;right:290px;top:118px;text-align:right;width:480px}
.hero .kicker{font-size:20px;font-style:italic;color:var(--teal)}
.hero .kicker b{color:var(--ink);font-weight:400}
.hero .deal{font-size:44px;font-weight:700;color:var(--teal);line-height:52px}
.hero .sub{font-size:18px;font-weight:600;color:var(--ink);padding-bottom:14px;border-bottom:1px solid #ccc}
.hero .headline{font-size:40px;font-weight:700;color:var(--ink);line-height:58px;border-bottom:1px solid #ccc;white-space:nowrap}
.hero .headline em{font-style:normal;color:var(--teal)}
.hero .cta{position:absolute;left:201px;top:351px;width:144px;height:39px;background:var(--teal);color:#fff;font-size:12px;display:flex;align-items:center;justify-content:center}
.hero .shot{position:absolute;left:517px;top:105px;width:270px;height:261px;background:linear-gradient(135deg,#1a1a1a 0 8%,#4c8a2e 30%,#a8d27a 55%,#2d5e1c 80%,#111 100%)}
.dots{position:absolute;left:270px;top:438px;display:flex;gap:6px}
.dots i{width:12px;height:4px;background:#ccc;display:block}
.dots i:first-child{background:#333}

/* sidebar */
.sidehead{position:absolute;left:50px;width:234px;height:49px;background:var(--teal);color:#fff;font-size:13px;font-weight:600;display:flex;align-items:center;justify-content:space-between;padding:0 22px}
.sidehead .arrows{display:flex;gap:10px}
.sidelist{position:absolute;left:50px;width:234px;display:flex;flex-direction:column;gap:20px}
.mini{position:relative;height:118px;background:#fff}
.mini .pic{position:absolute;left:14px;top:28px;width:86px;height:72px}
.sale{position:absolute;left:17px;top:-2px;width:34px;height:18px;background:var(--teal);color:#fff;font-size:8px;display:flex;align-items:center;justify-content:center}
.mini .info{position:absolute;left:114px;top:34px;font-size:11px}
.mini .price{color:var(--teal)}
.mini .price s{color:#555;text-decoration:none;margin-left:4px}
.mini .name{color:#555;margin-top:3px;text-transform:uppercase}
.stars{color:var(--teal);font-size:9px;letter-spacing:1px;margin-top:3px}

/* promo tiles */
.promo{position:absolute;top:765px;height:232px}
.promo.tv{left:334px;width:401px;background:var(--teal);color:#fff}
.promo.pc{left:752px;width:400px;background:#fff}
.promo h3{position:absolute;left:28px;top:20px;font-size:32px;font-weight:400;line-height:44px;white-space:nowrap;z-index:2}
.promo.pc h3{font-size:30px;color:var(--teal)}
.promo p{position:absolute;left:28px;top:68px;width:145px;font-size:11px;line-height:14px;z-index:2}
.promo.pc p{color:#444}
.promo .btn{position:absolute;left:28px;top:153px;width:98px;height:34px;font-size:11px;display:flex;align-items:center;justify-content:center;z-index:2}
.promo.tv .btn{background:#fff;color:var(--teal)}
.promo.pc .btn{background:var(--teal);color:#fff}
.promo .pic{position:absolute;z-index:1}

/* section titles */
.sectitle{position:absolute;font-size:22px;color:var(--ink);font-weight:400}
.sectitle em{font-style:normal;color:var(--teal)}
.rule{position:absolute;height:1px;background:var(--line)}
.sortby{position:absolute;left:1064px;top:1040px;width:84px;height:28px;background:#fff;border:1px solid #ddd;font-size:9px;color:#666;display:flex;align-items:center;justify-content:center;gap:6px}

/* product cards */
.grid{position:absolute;display:grid}
.grid.newest{left:334px;top:1105px;grid-template-columns:251px 252px 254px;column-gap:30px;row-gap:17px}
.grid.featured{left:50px;top:1969px;grid-template-columns:repeat(4,252px);column-gap:30px}
.card{position:relative;background:#fff;height:360px}
.featured .card{height:329px}
.card .pic{position:absolute;left:36px;top:18px;width:180px;height:180px;border-radius:2px}
.card .pic::after{content:"";position:absolute;left:-20px;right:-20px;bottom:-14px;height:8px;background:radial-gradient(ellipse at center,rgba(0,0,0,.12),rgba(0,0,0,0) 70%)}
.card .name{position:absolute;left:17px;top:218px;font-size:13px;color:#333}
.card .desc{position:absolute;left:17px;top:240px;width:220px;font-size:10px;line-height:13px;color:#888}
.card .cost{position:absolute;left:17px;top:285px;display:flex;align-items:baseline;gap:12px}
.card .cost s{font-size:12px;color:#999}
.card .cost b{font-size:18px;color:var(--teal);font-weight:600}
.card .actions{position:absolute;left:0;bottom:0;width:100%;height:39px;display:flex;font-size:10px;color:#fff}
.card .actions span{display:flex;align-items:center;gap:8px;padding-left:14px}
.card .buy{width:48%;background:var(--teal)}
.card .add{flex:1;background:var(--btn-gray)}
.card .preorder{position:absolute;left:17px;top:286px;width:118px;height:29px;border:1px solid var(--teal);color:var(--teal);font-size:10px;display:flex;align-items:center;justify-content:center}

/* image banners */
.showcase{position:absolute;top:2348px;width:356px;height:183px}
.showcase .frame{position:absolute;left:14px;top:14px;right:14px;bottom:14px;border:1px solid rgba(255,255,255,.35)}
.showcase .label{position:absolute;left:0;top:108px;width:212px;height:38px;background:var(--teal);color:#fff;font-size:18px;display:flex;align-items:center;justify-content:center}

/* newsletter */
.newsletter{position:absolute;left:0;top:2568px;width:1200px;height:174px;background:#fff}
.newsletter h2{position:absolute;left:187px;top:34px;font-size:34px;font-weight:300;color:var(--teal)}
.newsletter p{position:absolute;left:70px;top:90px;width:410px;text-align:center;font-size:13px;line-height:16px;color:#555}
.newsletter .email{position:absolute;left:517px;top:41px;width:246px;height:38px;border:1px solid #ccc;font-size:10px;color:#999;padding:12px 16px}
.newsletter .subscribe{position:absolute;left:517px;top:97px;width:246px;height:36px;background:#222;color:#fff;font-size:11px;display:flex;align-items:center;justify-content:center}
.newsletter .divider{position:absolute;left:821px;top:22px;width:1px;height:130px;background:#ddd}
.social{position:absolute;left:887px;top:34px;display:grid;grid-template-columns:repeat(3,48px);gap:12px 21px}
.social i{display:block;width:48px;height:48px;border-radius:50%;border:2px solid var(--teal)}

/* perks */
.perks{position:absolute;left:0;top:2742px;width:1200px;height:134px;background:var(--teal);display:flex}
.perk{position:relative;height:134px;display:flex;align-items:center;gap:20px;color:#fff;font-size:16px;font-weight:700;line-height:20px;text-transform:uppercase}
.perk+.perk{border-left:1px solid rgba(255,255,255,.3)}

/* footer */
.footer{position:absolute;left:0;top:2876px;width:1200px;height:286px;background:#111}
.fcol{position:absolute;top:72px}
.fcol h4{font-size:12px;font-weight:400;color:var(--teal);margin-bottom:24px}
.fcol li{list-style:none;font-size:11px;color:#9a9a9a;line-height:23px}
.fcol .contact li{display:flex;gap:12px;align-items:flex-start;line-height:16px;margin-bottom:14px}
.legal{position:absolute;left:0;top:3162px;width:1200px;height:70px;background:#080808}
.legal .copy{position:absolute;left:54px;top:27px;font-size:11px;color:#888}
.legal .mark{position:absolute;left:0;width:1200px;top:14px;text-align:center;font-size:34px;font-weight:700;color:#1e2e2b;letter-spacing:2px}
.cards{position:absolute;left:995px;top:20px;display:flex;gap:8px}
.cards i{display:block;width:44px;height:30px;background:#f2f2f2;border-radius:3px}
</style>
</head>
<body>

<header class="topbar">
  <div class="phone">
    <svg width="14" height="14" viewBox="0 0 24 24" fill="#1bb39a"><path d="M6.6 10.8a15 15 0 0 0 6.6 6.6l2.2-2.2a1 1 0 0 1 1-.25 11.4 11.4 0 0 0 3.6.57 1 1 0 0 1 1 1V20a1 1 0 0 1-1 1A17 17 0 0 1 3 4a1 1 0 0 1 1-1h3.5a1 1 0 0 1 1 1c0 1.25.2 2.45.57 3.57a1 1 0 0 1-.25 1z"/></svg>
    <span>1800 555 0147</span>
  </div>
  <nav class="links">
    <span>Login/Register</span><span>My Account</span><span>Wishlist - 0</span><span>Shopping TV - <em class="cart-total">$0.0</em></span>
  </nav>
  <div class="checkout">CHECKOUT
    <svg width="14" height="12" viewBox="0 0 14 12" fill="#fff"><path d="M0 4h8V0l6 6-6 6V8H0z"/></svg>
  </div>
</header>

<div class="masthead">
  <div class="brand">VOLTRIX STORE</div>
  <div class="search"><div class="field">Enter keyword</div><div class="go">SEARCH</div></div>
  <div class="currency">US Dollar $ <svg width="8" height="5" viewBox="0 0 8 5"><path d="M0 0l4 5 4-5" fill="none" stroke="#999"/></svg></div>
</div>

<nav class="mainnav">
  <div class="cat-toggle">
    <svg width="20" height="16" viewBox="0 0 20 16" fill="#fff"><rect width="20" height="2.5"/><rect y="6.7" width="20" height="2.5"/><rect y="13.5" width="20" height="2.5"/></svg>
    CATEGORIES
  </div>
  <div class="navlinks">
    <a style="width:100px"><svg width="20" height="17" viewBox="0 0 20 17" fill="#fff"><path d="M10 0l10 8h-3v9h-5v-6H8v6H3V8H0z"/></svg></a>
    <a style="width:122px">ABOUT US</a>
    <a style="width:95px">SHIPPING</a>
    <a style="width:108px">RETURNS</a>
    <a style="width:77px">FAQ</a>
    <a style="width:82px">BLOG</a>
    <a style="width:97px">EVENTS</a>
    <a style="width:116px">CONTACT US</a>
  </div>
</nav>

<div class="heroband"></div>
<ul class="catlist">
  <li>TV &amp; Video</li><li class="active">Mobile</li><li>Computing</li><li>Cameras &amp; Camcorders</li><li>Household Items</li><li>Kitchen Appliances</li><li>Mobile</li><li>Computing</li><li>Cameras</li>
</ul>

<section class="hero">
  <div class="copy">
    <div class="kicker">Electronics items <b>Offers</b></div>
    <div class="deal">25% OFF</div>
    <div class="sub">THE MARKED PRICE OF</div>
    <div class="headline">SUMMER <em>HOT OFFERS</em></div>
  </div>
  <div class="cta">SHOP NOW</div>
  <div class="shot" role="img" aria-label="Full HD flat-screen television showing a flower close-up"></div>
  <div class="dots"><i></i><i></i><i></i><i></i></div>
</section>

<!-- sidebar: specials -->
<div class="sidehead" style="top:765px">SPECIALS
  <span class="arrows"><svg width="10" height="6" viewBox="0 0 10 6"><path d="M1 1l4 4 4-4" fill="none" stroke="#fff" stroke-width="1.5"/></svg><svg width="10" height="6" viewBox="0 0 10 6"><path d="M1 5l4-4 4 4" fill="none" stroke="#fff" stroke-width="1.5"/></svg></span>
</div>
<div class="sidelist" style="top:825px">
  <div class="mini"><span class="sale">SALE</span><div class="pic" role="img" aria-label="Flat-screen TV" style="background:linear-gradient(135deg,#0e2a55,#2f86d6 55%,#0c1d3a)"></div><div class="info"><div class="price">$150.00<s>$199.99</s></div><div class="name">Mauris Gravida</div><div class="stars">★★★★★</div></div></div>
  <div class="mini"><span class="sale">SALE</span><div class="pic" role="img" aria-label="Smartphone" style="background:linear-gradient(135deg,#111,#3a3a3a 50%,#111)"></div><div class="info"><div class="price">$150.00<s>$199.99</s></div><div class="name">Mauris Gravida</div><div class="stars">★★★★★</div></div></div>
  <div class="mini"><span class="sale">SALE</span><div class="pic" role="img" aria-label="Blue headphones" style="background:linear-gradient(135deg,#e9eef5,#2a5fb0 50%,#e8edf4)"></div><div class="info"><div class="price">$150.00<s>$199.99</s></div><div class="name">Mauris Gravida</div><div class="stars">★★★★★</div></div></div>
  <div class="mini"><span class="sale">SALE</span><div class="pic" role="img" aria-label="Blue and white sewing machine" style="background:linear-gradient(135deg,#f1f3f6,#7fa6d9 55%,#eef1f5)"></div><div class="info"><div class="price">$150.00<s>$199.99</s></div><div class="name">Mauris Gravida</div><div class="stars">★★★★★</div></div></div>
</div>

<!-- sidebar: bestsellers -->
<div class="sidehead" style="top:1381px">BESTSELLERS
  <span class="arrows"><svg width="10" height="6" viewBox="0 0 10 6"><path d="M1 1l4 4 4-4" fill="none" stroke="#fff" stroke-width="1.5"/></svg><svg width="10" height="6" viewBox="0 0 10 6"><path d="M1 5l4-4 4 4" fill="none" stroke="#fff" stroke-width="1.5"/></svg></span>
</div>
<div class="sidelist" style="top:1450px">
  <div class="mini"><span class="sale">SALE</span><div class="pic" role="img" aria-label="Compact digital camera" style="background:linear-gradient(135deg,#2a2a2a,#6b5a3a 50%,#1a1a1a)"></div><div class="info"><div class="price">$150.00<s>$199.99</s></div><div class="name">Mauris Gravida</div><div class="stars">★★★★★</div></div></div>
  <div class="mini"><span class="sale">SALE</span><div class="pic" role="img" aria-label="Electric kettle" style="background:linear-gradient(135deg,#eee,#2b2b2b 50%,#f0f0f0)"></div><div class="info"><div class="price">$150.00<s>$199.99</s></div><div class="name">Mauris Gravida</div><div class="stars">★★★★★</div></div></div>
  <div class="mini"><span class="sale">SALE</span><div class="pic" role="img" aria-label="Inkjet printer" style="background:linear-gradient(135deg,#eaeaea,#1f1f1f 50%,#e9e9e9)"></div><div class="info"><div class="price">$150.00<s>$199.99</s></div><div class="name">Mauris Gravida</div><div class="stars">★★★★★</div></div></div>
</div>

<!-- promo tiles -->
<section class="promo tv">
  <h3>TV &amp; VIDEO</h3>
  <p>Lorem ipsum dolor sit amet, consectetur adipscing elit, sed do eiusmod tempor</p>
  <div class="btn">SHOP NOW</div>
  <div class="pic" role="img" aria-label="Full HD television with flower image" style="left:222px;top:52px;width:165px;height:160px;background:linear-gradient(135deg,#111 0 10%,#4c8a2e 35%,#b6dd84 60%,#111 100%)"></div>
</section>
<section class="promo pc">
  <h3>COMPUTING</h3>
  <p>Lorem ipsum dolor sit amet, consectetur adipscing elit, sed do eiusmod tempor</p>
  <div class="btn">SHOP NOW</div>
  <div class="pic" role="img" aria-label="Open laptop with tiled start screen" style="left:183px;top:70px;width:200px;height:125px;background:linear-gradient(160deg,#d9d9d9,#4a6fb8 40%,#2b2b2b 75%,#cfcfcf)"></div>
</section>

<!-- new products -->
<h2 class="sectitle" style="left:334px;top:1038px"><em>NEW</em> PRODUCTS</h2>
<div class="sortby">SORT BY <svg width="8" height="5" viewBox="0 0 8 5"><path d="M0 0l4 5 4-5" fill="none" stroke="#666"/></svg></div>
<div class="rule" style="left:334px;top:1078px;width:818px"></div>

<div class="grid newest">
  <article class="card"><div class="pic" role="img" aria-label="Wall-mounted flat-screen TV" style="background:linear-gradient(135deg,#1b1b1b,#6d7f86 50%,#2a2a2a)"></div><div class="name">Name of the product</div><div class="desc">Lorem ipsum dolor sit amet conse ctetur adipiscing elit, sed do eiusmodalique.</div><div class="cost"><s>$35.00</s><b>$ 29.00</b></div><div class="actions"><span class="buy"><svg width="11" height="11" viewBox="0 0 12 12"><rect width="12" height="12" rx="2" fill="#fff"/><path d="M3 6l2 2 4-4" fill="none" stroke="#1bb39a" stroke-width="1.6"/></svg>BUY NOW</span><span class="add"><svg width="12" height="11" viewBox="0 0 24 22" fill="#fff"><path d="M0 0h5l1 4h18l-3 10H8zM9 18a2 2 0 1 0 0 4 2 2 0 0 0 0-4zm10 0a2 2 0 1 0 0 4 2 2 0 0 0 0-4z"/></svg>ADD TO CART</span></div></article>
  <article class="card"><div class="pic" role="img" aria-label="Purple compact camera" style="background:linear-gradient(135deg,#f3f0f6,#5a3a7a 50%,#f1eef4)"></div><div class="name">Name of the product</div><div class="desc">Lorem ipsum dolor sit amet conse ctetur adipiscing elit, sed do eiusmodalique.</div><div class="cost"><s>$35.00</s><b>$ 29.00</b></div><div class="actions"><span class="buy"><svg width="11" height="11" viewBox="0 0 12 12"><rect width="12" height="12" rx="2" fill="#fff"/><path d="M3 6l2 2 4-4" fill="none" stroke="#1bb39a" stroke-width="1.6"/></svg>BUY NOW</span><span class="add"><svg width="12" height="11" viewBox="0 0 24 22" fill="#fff"><path d="M0 0h5l1 4h18l-3 10H8zM9 18a2 2 0 1 0 0 4 2 2 0 0 0 0-4zm10 0a2 2 0 1 0 0 4 2 2 0 0 0 0-4z"/></svg>ADD TO CART</span></div></article>
  <article class="card"><div class="pic" role="img" aria-label="Top-loading washing machine" style="background:linear-gradient(135deg,#eeeeee,#c9a3b0 55%,#9a3b55)"></div><div class="name">Name of the product</div><div class="desc">Lorem ipsum dolor sit amet conse ctetur adipiscing elit, sed do eiusmodalique.</div><div class="cost"><s>$35.00</s><b>$ 29.00</b></div><div class="actions"><span class="buy"><svg width="11" height="11" viewBox="0 0 12 12"><rect width="12" height="12" rx="2" fill="#fff"/><path d="M3 6l2 2 4-4" fill="none" stroke="#1bb39a" stroke-width="1.6"/></svg>BUY NOW</span><span class="add"><svg width="12" height="11" viewBox="0 0 24 22" fill="#fff"><path d="M0 0h5l1 4h18l-3 10H8zM9 18a2 2 0 1 0 0 4 2 2 0 0 0 0-4zm10 0a2 2 0 1 0 0 4 2 2 0 0 0 0-4z"/></svg>ADD TO CART</span></div></article>
  <article class="card"><div class="pic" role="img" aria-label="Induction cooktop" style="background:linear-gradient(135deg,#f2f2f2,#1e2330 45%,#3a4a66 70%,#f0f0f0)"></div><div class="name">Name of the product</div><div class="desc">Lorem ipsum dolor sit amet conse ctetur adipiscing elit, sed do eiusmodalique.</div><div class="cost"><s>$35.00</s><b>$ 29.00</b></div><div class="actions"><span class="buy"><svg width="11" height="11" viewBox="0 0 12 12"><rect width="12" height="12" rx="2" fill="#fff"/><path d="M3 6l2 2 4-4" fill="none" stroke="#1bb39a" stroke-width="1.6"/></svg>BUY NOW</span><span class="add"><svg width="12" height="11" viewBox="0 0 24 22" fill="#fff"><path d="M0 0h5l1 4h18l-3 10H8zM9 18a2 2 0 1 0 0 4 2 2 0 0 0 0-4zm10 0a2 2 0 1 0 0 4 2 2 0 0 0 0-4z"/></svg>ADD TO CART</span></div></article>
  <article class="card"><div class="pic" role="img" aria-label="Black stereo speaker system" style="background:linear-gradient(135deg,#f0f0f0,#121212 35%,#2e2e2e 65%,#f0f0f0)"></div><div class="name">Name of the product</div><div class="desc">Lorem ipsum dolor sit amet conse ctetur adipiscing elit, sed do eiusmodalique.</div><div class="cost"><s>$35.00</s><b>$ 29.00</b></div><div class="actions"><span class="buy"><svg width="11" height="11" viewBox="0 0 12 12"><rect width="12" height="12" rx="2" fill="#fff"/><path d="M3 6l2 2 4-4" fill="none" stroke="#1bb39a" stroke-width="1.6"/></svg>BUY NOW</span><span class="add"><svg width="12" height="11" viewBox="0 0 24 22" fill="#fff"><path d="M0 0h5l1 4h18l-3 10H8zM9 18a2 2 0 1 0 0 4 2 2 0 0 0 0-4zm10 0a2 2 0 1 0 0 4 2 2 0 0 0 0-4z"/></svg>ADD TO CART</span></div></article>
  <article class="card"><div class="pic" role="img" aria-label="Home theatre projector" style="background:linear-gradient(135deg,#f2f2f2,#1a1a1a 45%,#444 70%,#f0f0f0)"></div><div class="name">Name of the product</div><div class="desc">Lorem ipsum dolor sit amet conse ctetur adipiscing elit, sed do eiusmodalique.</div><div class="cost"><s>$35.00</s><b>$ 29.00</b></div><div class="actions"><span class="buy"><svg width="11" height="11" viewBox="0 0 12 12"><rect width="12" height="12" rx="2" fill="#fff"/><path d="M3 6l2 2 4-4" fill="none" stroke="#1bb39a" stroke-width="1.6"/></svg>BUY NOW</span><span class="add"><svg width="12" height="11" viewBox="0 0 24 22" fill="#fff"><path d="M0 0h5l1 4h18l-3 10H8zM9 18a2 2 0 1 0 0 4 2 2 0 0 0 0-4zm10 0a2 2 0 1 0 0 4 2 2 0 0 0 0-4z"/></svg>ADD TO CART</span></div></article>
</div>

<!-- featured products -->
<h2 class="sectitle" style="left:50px;top:1904px"><em>FEATURED</em> PRODUCTS</h2>
<div class="grid featured">
  <article class="card"><div class="pic" role="img" aria-label="Espresso coffee machine" style="top:25px;height:160px;background:linear-gradient(135deg,#f2f2f2,#1c1c1c 45%,#8a8a8a 70%,#f0f0f0)"></div><div class="name">Product Name Here</div><div class="desc">Lorem ipsum dolor sit amet conse ctetur adipiscing elit, sed do eiusmodalique.</div><div class="preorder">PRE-ORDER NOW</div></article>
  <article class="card"><div class="pic" role="img" aria-label="Desktop computer tower with monitor" style="top:25px;height:160px;background:linear-gradient(135deg,#f2f2f2,#0f1a2e 40%,#2c6bd0 65%,#f0f0f0)"></div><div class="name">Product Name Here</div><div class="desc">Lorem ipsum dolor sit amet conse ctetur adipiscing elit, sed do eiusmodalique.</div><div class="preorder">PRE-ORDER NOW</div></article>
  <article class="card"><div class="pic" role="img" aria-label="Wall-mounted air conditioner" style="top:25px;height:160px;background:linear-gradient(160deg,#f3f3f3,#e6e6e6 45%,#6a1f24 65%,#f2f2f2)"></div><div class="name">Product Name Here</div><div class="desc">Lorem ipsum dolor sit amet conse ctetur adipiscing elit, sed do eiusmodalique.</div><div class="preorder">PRE-ORDER NOW</div></article>
  <article class="card"><div class="pic" role="img" aria-label="Magenta refrigerator" style="top:25px;height:160px;background:linear-gradient(135deg,#f2f2f2,#8a1450 45%,#c2307a 65%,#f0f0f0)"></div><div class="name">Product Name Here</div><div class="desc">Lorem ipsum dolor sit amet conse ctetur adipiscing elit, sed do eiusmodalique.</div><div class="preorder">PRE-ORDER NOW</div></article>
</div>

<!-- image banners -->
<section class="showcase" style="left:47px" role="img" aria-label="Flat-lay of dark accessories: wallet, headphones, watch"><div style="position:absolute;inset:0;background:linear-gradient(135deg,#2a2a2a,#4a4744 50%,#1e1e1e)"></div><div class="frame"></div><div class="label">ACCESORIES</div></section>
<section class="showcase" style="left:422px" role="img" aria-label="Friends sharing devices on a summer day"><div style="position:absolute;inset:0;background:linear-gradient(135deg,#5a4330,#9a7a58 50%,#3a2c22)"></div><div class="frame"></div><div class="label">SUMMER OFFER</div></section>
<section class="showcase" style="left:797px" role="img" aria-label="Kitchen with stainless-steel home appliances"><div style="position:absolute;inset:0;background:linear-gradient(135deg,#1e2a38,#4a5868 50%,#18202a)"></div><div class="frame"></div><div class="label">HOME APPLIANCES</div></section>

<!-- newsletter -->
<section class="newsletter">
  <h2>Newsletter Sign Up</h2>
  <p>Lorem ipsum dolor sit amet conse ctetur adipiscing elit, sed do eiusmod tempor incididunt ut labore et dolore magna aliqua.</p>
  <div class="email">ENTER YOUR EMAIL ADDRESS</div>
  <div class="subscribe">SUBSCRIBE</div>
  <div class="divider"></div>
  <div class="social"><i></i><i></i><i></i><i></i><i></i><i></i></div>
</section>

<!-- perks -->
<section class="perks">
  <div class="perk" style="width:388px;padding-left:80px">
    <svg width="42" height="40" viewBox="0 0 24 22" fill="#fff"><path d="M0 9h5v13H0zM7 21V9l5-9c1.6 0 2.6 1.2 2.3 2.8L13.6 7H21a3 3 0 0 1 2.9 3.6l-2 8.6A3.6 3.6 0 0 1 18.4 22H8z"/></svg>
    <div>SATISFACTION<br>100% GUARANTEED</div>
  </div>
  <div class="perk" style="width:392px;padding-left:78px">
    <svg width="46" height="34" viewBox="0 0 30 22" fill="#fff"><path d="M0 0h18v15H0zM19 5h6l5 6v4h-11zM6 16a3 3 0 1 0 .001 6A3 3 0 0 0 6 16zm17 0a3 3 0 1 0 .001 6A3 3 0 0 0 23 16z"/></svg>
    <div>FREE SHIPPING<br>ON ORDERS OVER $99</div>
  </div>
  <div class="perk" style="flex:1;padding-left:64px">
    <svg width="40" height="40" viewBox="0 0 24 24" fill="none" stroke="#fff" stroke-width="3"><path d="M20 9A8.5 8.5 0 0 0 5 6.5M4 15a8.5 8.5 0 0 0 15 2.5"/><path d="M4 2v5h5M20 22v-5h-5" stroke-width="2.6"/></svg>
    <div>7 DAY<br>EASY RETURN</div>
  </div>
</section>

<!-- footer -->
<footer class="footer">
  <div class="fcol" style="left:54px"><h4>INFORMATION</h4><ul><li>ABOUT US</li><li>CUSTOMER SERVICE</li><li>PRIVACY POLICY</li><li>SEARCH TERMS</li><li>ORDERS AND RETURNS</li><li>CONTACT US</li></ul></div>
  <div class="fcol" style="left:323px"><h4>WHY BUY FROM US</h4><ul><li>SHIPPING &amp; RETURNS</li><li>SECURE SHOPPING</li><li>INTERNATIONAL SHIPPING</li><li>AFFILIATES</li><li>GROUP SALES</li></ul></div>
  <div class="fcol" style="left:625px"><h4>MY ACCOUNT</h4><ul><li>SIGN IN</li><li>VIEW CART</li><li>MY WISHLIST</li><li>TRACK MY ORDER</li><li>HELP</li></ul></div>
  <div class="fcol" style="left:868px"><h4>CONTACTS</h4>
    <ul class="contact">
      <li><svg width="10" height="14" viewBox="0 0 10 14" fill="#9a9a9a"><path d="M5 0a5 5 0 0 0-5 5c0 3.8 5 9 5 9s5-5.2 5-9a5 5 0 0 0-5-5zm0 7a2 2 0 1 1 0-4 2 2 0 0 1 0 4z"/></svg><span>12 LARKSPUR LANE, NORTHFIELD NF4 2KD<br>P. O BOX 40811, COUNTRY</span></li>
      <li><svg width="12" height="12" viewBox="0 0 24 24" fill="#9a9a9a"><path d="M6.6 10.8a15 15 0 0 0 6.6 6.6l2.2-2.2a1 1 0 0 1 1-.25 11.4 11.4 0 0 0 3.6.57 1 1 0 0 1 1 1V20a1 1 0 0 1-1 1A17 17 0 0 1 3 4a1 1 0 0 1 1-1h3.5a1 1 0 0 1 1 1c0 1.25.2 2.45.57 3.57a1 1 0 0 1-.25 1z"/></svg><span>CALL US: (800) 555-0192</span></li>
      <li><svg width="13" height="10" viewBox="0 0 13 10" fill="#9a9a9a"><path d="M0 0h13v1.5L6.5 5.5 0 1.5zM0 3l6.5 4L13 3v7H0z"/></svg><span>EMAIL INFO@VOLTRIXSTORE.COM</span></li>
    </ul>
  </div>
</footer>

<div class="legal">
  <div class="copy">All Rights Reserved. Copyrights @ 2015</div>
  <div class="mark">VOLTRIX STORE</div>
  <div class="cards"><i></i><i></i><i></i></div>
</div>

</body>
</html>
```